We sell companies excess stock for them

We need a business card for a company based in New Zealand called 'StockHarbor'.

Check out our website to get an idea www.stockharbor.example

We help other businesses to;
- Sell Excess Stock
- Manage Product Returns
- Sell Company Assets

Our logo is attached for your reference
The font used is 'RifficFree-Bold'

Target Market(s)

Businesses

Industry/Entity Type

Business

Contact Information for Business Card

Name: Mark Pellow
Phone: 027 846 2093
email: markpellow@stockharbor.example
website: www.stockharbor.example

Font styles to use
Other font styles liked:
• Unsure

Colors
9bcb3b

Requirements
Must have
• coming soon
Nice to have
• coming soon
Should not have
• coming soon

```html
<!DOCTYPE html>
<html lang="en">
<head>
<meta charset="utf-8">
<title>StockHarbor Business Card</title>
<link rel="stylesheet" href="https://fonts.googleapis.com/css2?family=Fredoka:wght@700&family=Roboto:wght@400&display=swap">
<style>
  :root {
    --green: #8fbe3f;
    --green-deep: #7aa930;
    --charcoal: #333335;
    --white: #ffffff;
    --page: #ecebe8;
    --mascot-orange: #f0a640;
    --mascot-green: #6fae3a;
  }
  * { box-sizing: border-box; margin: 0; padding: 0; }
  html, body {
    width: 1200px; height: 1200px; overflow: hidden;
    background: var(--page);
  }
  .canvas {
    position: relative; width: 1200px; height: 1200px;
  }
  .card {
    position: absolute; left: 150px; width: 900px; height: 515px;
    overflow: hidden; border-radius: 4px;
    box-shadow: 0 10px 30px rgba(0,0,0,0.18);
    background: var(--charcoal);
  }
  .card--front { top: 60px; }
  .card--back { top: 625px; }
  .card__shapes { position: absolute; inset: 0; width: 100%; height: 100%; }
  .mascot {
    position: absolute; border-radius: 40px;
    background: radial-gradient(circle at 45% 40%, var(--mascot-orange) 0%, var(--mascot-green) 75%);
    opacity: 0.95;
  }
  .card--front .mascot { left: 330px; top: 55px; width: 250px; height: 285px; }
  .card--back .mascot { left: 610px; top: 40px; width: 240px; height: 290px; }
  .brand-name {
    position: absolute; font-family: 'Fredoka', sans-serif; font-weight: 700;
    color: var(--white); line-height: 1; white-space: nowrap;
  }
  .card--front .brand-name { left: 0; right: 0; top: 355px; text-align: center; font-size: 104px; }
  .card--back .brand-name { left: 70px; top: 70px; font-size: 66px; }
  .contact-list {
    position: absolute; left: 72px; top: 195px; list-style: none;
    font-family: 'Roboto', sans-serif; font-size: 31px; color: var(--white);
  }
  .contact-item { display: flex; align-items: center; height: 62px; }
  .contact-icon {
    width: 46px; height: 46px; margin-right: 18px; flex: none;
    border: 2.5px solid var(--white); border-radius: 50%;
    display: flex; align-items: center; justify-content: center;
  }
  .contact-icon svg { width: 24px; height: 24px; fill: none; stroke: var(--white); stroke-width: 2; stroke-linecap: round; stroke-linejoin: round; }
  .contact-icon .solid { fill: var(--white); stroke: none; }
</style>
</head>
<body>
<main class="canvas">

  <section class="card card--front" aria-label="Business card front">
    <svg class="card__shapes" viewBox="0 0 900 515" preserveAspectRatio="none" aria-hidden="true">
      <rect width="900" height="515" fill="var(--green)"/>
      <path d="M0,135 C260,150 430,330 900,165 L900,515 L0,515 Z" fill="var(--white)"/>
      <path d="M0,205 C260,215 440,345 900,172 L900,515 L0,515 Z" fill="var(--charcoal)"/>
    </svg>
    <div class="mascot" role="img" aria-label="Cartoon courier mascot in a green cap carrying an orange parcel, giving a thumbs up"></div>
    <h1 class="brand-name">StockHarbor</h1>
  </section>

  <section class="card card--back" aria-label="Business card back">
    <svg class="card__shapes" viewBox="0 0 900 515" preserveAspectRatio="none" aria-hidden="true">
      <rect width="900" height="515" fill="var(--charcoal)"/>
      <path d="M505,0 C555,230 730,395 900,445 L900,0 Z" fill="var(--white)"/>
      <path d="M555,0 C610,215 760,375 900,425 L900,0 Z" fill="var(--green)"/>
    </svg>
    <div class="mascot" role="img" aria-label="Cartoon courier mascot in a green cap carrying an orange parcel, giving a thumbs up"></div>
    <h2 class="brand-name">StockHarbor</h2>
    <ul class="contact-list">
      <li class="contact-item">
        <span class="contact-icon"><svg viewBox="0 0 24 24"><circle class="solid" cx="12" cy="7" r="4"/><path class="solid" d="M5,22 C5,15 8,12.5 12,12.5 C16,12.5 19,15 19,22 Z"/></svg></span>
        Mark Pellow
      </li>
      <li class="contact-item">
        <span class="contact-icon"><svg viewBox="0 0 24 24"><path d="M6,3 L9,3 L10.5,7.5 L8.5,9 C9.5,11.5 12.5,14.5 15,15.5 L16.5,13.5 L21,15 L21,18 C21,19.5 19.5,21 18,21 C10,20.5 3.5,14 3,6 C3,4.5 4.5,3 6,3 Z"/></svg></span>
        027 846 2093
      </li>
      <li class="contact-item">
        <span class="contact-icon"><svg viewBox="0 0 24 24"><circle cx="12" cy="12" r="9"/><ellipse cx="12" cy="12" rx="4" ry="9"/><line x1="3" y1="12" x2="21" y2="12"/></svg></span>
        www.stockharbor.example
      </li>
      <li class="contact-item">
        <span class="contact-icon"><svg viewBox="0 0 24 24"><rect x="3" y="6" width="18" height="12" rx="1"/><path d="M3,6 L12,13 L21,6"/></svg></span>
        markpellow@stockharbor.example
      </li>
    </ul>
  </section>

</main>
</body>
</html>
```